Quiz Arena Clash Halls Initial Post Card

Looking for an oversized post card design to send out via RMSR with NPDS. Looking for this postcard to match the look and feel of our logo/website. This is a new business that we are launching and this is the first piece of marketing we are working on to get our name out there. See below for additional requirements of the postcard.

1. Must match the look and feel of our website/logo
2. Must have two coupons outlined - details on both are attached
3. Must have callout somewhere - that stands out - that says "#1 New Experience in the Twin Cities"
4. Must call out "Great for team building, work outings,birthday celebrations, or just for fun with friends and family!"
5. Call out "Private team building events available upon request" and "Online bookings available now!"
6. Call out in big letters "Finally YOU"RE ALL IN in the GAME SHOW!"
7. Callout website - www.quizarenaclashhalls.example, Phone # 612-555-0147, facebook @QuizArenaClashHalls, Address: 4215 Larkmoor Ave N, Cedar Hollow, MN
8. Must callout the requirements for RMSR - let me know if you are not aware of these. I have attached for reference.

Check out: www.quizarenaclashhalls.example for inspiration/direction.

Industry/Entity Type

Entertainment

Requirements
Must have
• Simple - not too crowded of a design. Call to action to check out our website/give us a call!
Should not have
• Too busy of a design - text everywhere is not okay.

```html
<!DOCTYPE html>
<html lang="en">
<head>
<meta charset="utf-8">
<title>Quiz Arena Clash Halls – Postcard</title>
<link rel="stylesheet" href="https://fonts.googleapis.com/css2?family=Montserrat:wght@400;500;600;700;800;900&family=Roboto:wght@400;500;700&display=swap">
<style>
  :root {
    --page: #e6e6e8;
    --navy: #17142a;
    --navy-deep: #0f0d1d;
    --violet: #7a4bb8;
    --white: #ffffff;
    --gold: #f5d20a;
    --cream: #e9dfa0;
    --ticket-blue: #1d5f96;
    --ticket-edge: #f06b2c;
    --ticket-yellow: #f7d21c;
    --cyan: #3ec6f2;
    --red: #e0262b;
    --pink: #f04a7a;
    --orange: #f6a21e;
    --ink: #222222;
  }
  * { margin: 0; padding: 0; box-sizing: border-box; }
  html, body { width: 947px; height: 1200px; overflow: hidden; }
  body { background: var(--page); font-family: "Montserrat", sans-serif; position: relative; }

  .card {
    position: absolute; left: 50px; width: 806px; height: 522px; overflow: hidden;
    background:
      radial-gradient(ellipse 420px 160px at 86% 52%, rgba(122,75,184,.55), transparent 70%),
      radial-gradient(ellipse 300px 110px at 20% 80%, rgba(70,50,140,.35), transparent 70%),
      var(--navy);
    color: var(--white);
  }
  .card--front { top: 50px; }
  .card--back { top: 619px;
    background:
      radial-gradient(ellipse 380px 150px at 70% 22%, rgba(122,75,184,.5), transparent 70%),
      radial-gradient(ellipse 300px 120px at 95% 60%, rgba(122,75,184,.45), transparent 70%),
      var(--navy);
  }
  .abs { position: absolute; }

  /* Front */
  .brand-name {
    left: 0; right: 0; top: 130px; text-align: center;
    font-weight: 800; font-size: 46px; letter-spacing: 1px; color: var(--white);
  }
  .tagline-lead { left: 0; right: 0; top: 303px; text-align: center; font-size: 24px; font-weight: 500; letter-spacing: 1.5px; }
  .tagline-main {
    left: 0; right: 0; top: 327px; text-align: center; font-size: 52px; font-weight: 900; letter-spacing: 1px;
    color: #f1f1f1; text-shadow: 0 3px 0 #777, 0 5px 8px rgba(0,0,0,.6);
  }
  .booking-box {
    left: 177px; top: 405px; width: 452px; height: 56px; border: 1px dashed var(--gold); border-radius: 6px;
    text-align: center; font-family: "Roboto", sans-serif;
  }
  .booking-box .private { color: var(--cyan); font-size: 16.5px; margin-top: 5px; }
  .booking-box .online { color: var(--gold); font-size: 22px; font-weight: 700; line-height: 1.05; }
  .website { left: 0; right: 0; top: 469px; text-align: center; font-size: 25px; font-weight: 500; color: var(--cream); }

  .ticket {
    top: 338px; width: 131px; height: 184px; background: var(--ticket-blue);
    border-left: 3px solid var(--ticket-edge); border-right: 3px solid var(--ticket-yellow);
    text-align: center; font-family: "Roboto", sans-serif;
  }
  .ticket--small { left: 30px; }
  .ticket--large { left: 646px; }
  .ticket::before, .ticket::after {
    content: ""; position: absolute; top: 43px; width: 18px; height: 30px; background: var(--navy); border-radius: 50%;
  }
  .ticket::before { left: -12px; }
  .ticket::after { right: -12px; }
  .ticket-head { font-family: "Montserrat", sans-serif; font-weight: 800; font-size: 20px; line-height: 21px; margin-top: 22px; }
  .ticket-value { font-family: "Montserrat", sans-serif; font-weight: 900; font-size: 38px; line-height: 40px; color: #e8e8e8; margin-top: 4px; }
  .ticket-value sup { font-size: 20px; vertical-align: 14px; }
  .ticket-value small { font-size: 13px; color: var(--orange); font-weight: 700; margin-left: -6px; }
  .ticket-foot { position: absolute; left: 0; right: 0; bottom: 0; height: 68px; background: #2a78b4; padding-top: 4px; }
  .ticket-code { font-size: 7.5px; color: var(--gold); font-weight: 500; }
  .ticket-terms { font-size: 10.5px; line-height: 13px; margin-top: 6px; padding: 0 6px; }

  /* Back */
  .finally {
    left: 30px; top: 33px; width: 40px; height: 196px;
  }
  .finally span {
    position: absolute; left: 50%; top: 50%; transform: translate(-50%,-50%) rotate(-90deg);
    font-weight: 900; font-size: 42px; letter-spacing: 1px; color: var(--cream); white-space: nowrap;
  }
  .all-in { left: 76px; top: 20px; font-size: 29px; font-weight: 500; letter-spacing: .5px; }
  .big-word {
    left: 74px; width: 340px; text-align: center; font-weight: 900; font-size: 94px; line-height: 1; letter-spacing: -1px;
    color: #f4f4ff; text-shadow: 0 0 10px rgba(180,200,255,.7);
  }
  .big-word--game { top: 56px; }
  .big-word--show { top: 150px; }
  .uses { left: 40px; width: 360px; top: 277px; text-align: center; font-weight: 800; font-size: 21.5px; line-height: 28px; }
  .uses .hl { color: var(--red); }

  .contact { left: 18px; top: 432px; font-family: "Roboto", sans-serif; }
  .contact-title { font-size: 17px; font-weight: 500; color: var(--pink); margin-bottom: 4px; }
  .contact-title b { color: var(--gold); font-weight: 500; }
  .contact-row { display: flex; align-items: center; gap: 9px; font-size: 16px; height: 23.5px; }
  .contact-row.bold { font-weight: 700; font-size: 17px; }
  .contact-row svg { width: 13px; height: 13px; flex: none; }
  .dot { width: 13px; height: 13px; border-radius: 50%; background: var(--gold); flex: none; }

  .indicia-frame { left: 676px; top: 14px; width: 115px; height: 115px; background: var(--white); padding: 7px; }
  .indicia {
    width: 100%; height: 100%; border: 1px solid var(--ink); color: var(--ink);
    font-family: "Roboto", sans-serif; font-size: 11.5px; line-height: 17.5px; text-align: center; padding-top: 10px;
  }
  .mail-panel { left: 538px; top: 229px; width: 253px; height: 280px; background: var(--white); }
  .barcode-strip { left: 351px; top: 451px; width: 440px; height: 58px; background: var(--white); }
  .barcode-label {
    left: 351px; top: 472px; width: 440px; text-align: center; font-family: "Roboto", sans-serif;
    font-size: 13px; letter-spacing: 5px; color: #888;
  }
  .recipient {
    left: 556px; top: 246px; width: 219px; height: 52px; border: 1px solid var(--ink); color: var(--ink);
    font-family: "Roboto", sans-serif; font-size: 14px; line-height: 20px; padding: 4px 10px;
  }
  .address-line { left: 558px; width: 212px; height: 1px; background: var(--ink); }
</style>
</head>
<body>

<section class="card card--front" aria-label="Postcard front">
  <div class="abs brand-name">Quiz Arena Clash Halls</div>

  <div class="abs tagline-lead">#1 New Experience in the</div>
  <div class="abs tagline-main">TWIN CITIES</div>

  <div class="abs booking-box">
    <p class="private">Private team building events available upon request and</p>
    <p class="online">ONLINE BOOKINGS AVAILABLE NOW!</p>
  </div>
  <div class="abs website">www.quizarenaclashhalls.example</div>

  <div class="abs ticket ticket--small">
    <p class="ticket-head">GET<br>TICKETS</p>
    <p class="ticket-value">20<sup>%</sup><small>OFF</small></p>
    <div class="ticket-foot">
      <p class="ticket-code">CODE: 20OFFOCTNOV</p>
      <p class="ticket-terms">a booking of less than 10 people in Oct or Nov of 2017</p>
    </div>
  </div>

  <div class="abs ticket ticket--large">
    <p class="ticket-head">GET<br>TICKETS</p>
    <p class="ticket-value">50<sup>%</sup><small>OFF</small></p>
    <div class="ticket-foot">
      <p class="ticket-code">CODE: $50OFFOCTNOV</p>
      <p class="ticket-terms">a booking of 10 or more people in Oct or Nov 2017</p>
    </div>
  </div>
</section>

<section class="card card--back" aria-label="Postcard back">
  <div class="abs finally"><span>FINALLY</span></div>
  <div class="abs all-in">YOU"RE ALL IN IN THE</div>
  <div class="abs big-word big-word--game">GAME</div>
  <div class="abs big-word big-word--show">SHOW!</div>

  <div class="abs uses">
    <span class="hl">GREAT FOR TEAM BUILDING, WORK OUTINGS,BIRTHDAY CELEBRATIONS, OR</span><br>
    JUST FOR FUN WITH FRIENDS AND FAMILY!
  </div>

  <div class="abs contact">
    <p class="contact-title">KEEP IN <b>TOUCH</b></p>
    <p class="contact-row">
      <svg viewBox="0 0 12 12"><path d="M6 0.5a4 4 0 0 0-4 4c0 3 4 7 4 7s4-4 4-7a4 4 0 0 0-4-4z" fill="#f5d20a"/><circle cx="6" cy="4.5" r="1.5" fill="#17142a"/></svg>
      4215 Larkmoor Ave N, Cedar Hollow, MN
    </p>
    <p class="contact-row bold">
      <svg viewBox="0 0 12 12"><circle cx="6" cy="6" r="6" fill="#f5d20a"/><path d="M3.8 3.2l1.2-.3.7 1.6-.8.6a4 4 0 0 0 1.9 1.9l.6-.8 1.6.7-.3 1.2c-2.8.3-5.3-2.2-4.9-4.9z" fill="#17142a"/></svg>
      612-555-0147
    </p>
    <p class="contact-row"><span class="dot"></span>@QuizArenaClashHalls</p>
  </div>

  <div class="abs indicia-frame">
    <div class="indicia">PRSRT STD<br>ECRWSS U.S.<br>POSTAGE<br>PAID&nbsp; RMSR<br>RETAIL</div>
  </div>

  <div class="abs mail-panel"></div>
  <div class="abs barcode-strip"></div>
  <div class="abs barcode-label">BARCODE AREA</div>
  <div class="abs recipient">Local<br>Postal Customer</div>
  <div class="abs address-line" style="top:341px"></div>
  <div class="abs address-line" style="top:377px"></div>
  <div class="abs address-line" style="top:410px"></div>
</section>

</body>
</html>
```